(Wix) Website Design Tweaks

The site: www.LanternAndLoomly.com
(The coding must be done within Wix. I will create a duplicate website so you can gain access and begin editing.)

My website contains my preferred text and images - but it needs to look more professional. My business focuses on "Corporate Messaging" and "Marketing Communications", so the website needs to look professional, but not too corporate. My clients range from very big companies to technology startups - the look and feel should be uncluttered, professional, and modern.

I want someone to review the pages, and make changes / suggestions focused on:
1) Fonts
2) Colors
3) Layout

If you have ideas for adding additional graphics, that's fine, but they should be consistent with what I already have . . . unless you think some / all of my images need to be changed.

My site is very, very small, and only contains 5 (very short) pages. There are no sub-pages. (One page is the contact page, with almost nothing except form fields.)

If you do a good job with my site, I may be able to provide you with additional work - many of my clients need website design tweaks, after I provide the verbiage.

```html
<!DOCTYPE html>
<html lang="en">
<head>
<meta charset="utf-8">
<title>Lantern &amp; Loomly</title>
<link href="https://fonts.googleapis.com/css2?family=Montserrat:ital,wght@0,300;0,400;0,500;0,600;0,700;0,800;1,400&display=swap" rel="stylesheet">
<style>
:root{
  --blue:#00aeef;
  --blue-deep:#0a6fb0;
  --ink:#1f1f22;
  --text:#3a3a3f;
  --muted:#6b6b72;
  --hero:#1d1d20;
  --footer:#1f2023;
  --footer-base:#141416;
  --tint:#eef3fa;
  --white:#ffffff;
}
*{box-sizing:border-box;margin:0;padding:0}
html,body{width:1200px;height:3971px;overflow:hidden}
body{font-family:'Montserrat',sans-serif;color:var(--text);background:var(--white);position:relative}
.abs{position:absolute}
.photo{position:absolute;box-shadow:0 8px 22px rgba(0,0,0,.18);border:3px solid var(--white)}
.btn{position:absolute;display:flex;align-items:center;justify-content:center;font-size:13px;font-weight:600;border-radius:0 14px 0 14px;background:var(--blue);color:var(--white)}
.eyebrow{position:absolute;font-size:12px;font-weight:500;color:var(--blue);text-transform:uppercase;letter-spacing:.3px}
.title{position:absolute;font-size:31px;font-weight:400;color:var(--ink);line-height:36px}
.title b{font-weight:800}
.copy{position:absolute;font-size:11.5px;line-height:22.5px;color:var(--text)}

/* hero */
.hero{position:absolute;left:0;top:0;width:1200px;height:628px;background:var(--hero)}
.hero-photo{position:absolute;left:682px;top:0;width:518px;height:712px;border-bottom-left-radius:190px;background:linear-gradient(135deg,#0b4f7d 0%,#0a86c6 45%,#0c5d92 100%)}
.brand-box{position:absolute;left:159px;top:18px;width:102px;height:102px;background:var(--blue);color:var(--white);font-size:17px;line-height:20px;font-weight:400;padding:52px 0 0 8px}
.nav{position:absolute;top:58px;font-size:11.5px;font-weight:600;color:var(--white)}
.join{position:absolute;left:907px;top:49px;width:129px;height:40px;background:var(--white);color:var(--blue);font-size:13px;font-weight:500;display:flex;align-items:center;justify-content:center;border-radius:0 16px 0 16px}
.hero-title{position:absolute;left:162px;top:188px;font-size:46px;line-height:54px;color:var(--white);font-weight:300}
.hero-title b{font-weight:700}
.hero-copy{position:absolute;left:164px;top:364px;width:270px;font-size:12px;line-height:19px;color:#e6e6e6}
.btn-ghost{background:transparent;border:1.5px solid var(--white)}
.partners{position:absolute;left:138px;top:656px;display:flex;gap:30px;align-items:center}
.partners span{display:block;width:38px;height:36px;background:#d3d5d9;border-radius:4px}
.partners span.round{border-radius:50%}

/* services */
.services{position:absolute;left:0;top:1676px;width:1200px;height:700px;background:var(--tint)}
.card-img{position:absolute;width:206px;height:145px}
.card-label{position:absolute;width:206px;text-align:center;font-size:14.5px;line-height:18px;color:var(--ink)}

/* testimonials */
.t-card{position:absolute;background:var(--white);box-shadow:0 6px 24px rgba(20,40,80,.12);padding:36px 20px 0 18px}
.t-quote{font-size:14px;font-style:italic;line-height:22.5px;color:var(--muted)}
.t-name{font-size:14.5px;font-weight:700;color:var(--ink);margin-top:22px}
.t-role{font-size:10.5px;line-height:12px;color:var(--muted)}
.qmark{position:absolute;top:-22px;right:34px}

/* footer */
.footer{position:absolute;left:0;top:3485px;width:1200px;height:486px;background:var(--footer)}
.footer-base{position:absolute;left:0;top:3898px;width:1200px;height:73px;background:var(--footer-base)}
.join-box{position:absolute;left:191px;top:3369px;width:816px;height:239px;border-radius:70px 0 70px 0;background:linear-gradient(100deg,#08a6ea 0%,#0aa0e6 55%,#0a7fc7 100%);overflow:hidden}
.field{position:absolute;height:40px;background:var(--white);border-radius:0 12px 0 12px;font-size:12.5px;color:#888;padding:12px 0 0 18px}
.f-head{position:absolute;font-size:15px;font-weight:600;color:var(--white)}
.f-link{position:absolute;font-size:11.5px;color:#e0e0e0}
.social{position:absolute;top:3829px;width:12px;height:12px;border-radius:50%;background:#e8e8e8}
</style>
</head>
<body>

<!-- HERO -->
<section class="hero" aria-label="Hero"></section>
<div class="hero-photo" role="img" aria-label="Blue-toned photo of a presenter at a flip chart in a meeting room"></div>
<div class="brand-box">LANTERN &amp;<br>LOOMLY</div>
<nav>
  <span class="nav" style="left:426px">HOME</span>
  <span class="nav" style="left:504px">LOOMCAMP</span>
  <span class="nav" style="left:617px">TESTIMONIALS</span>
  <span class="nav" style="left:746px">TEAM</span>
  <span class="nav" style="left:820px">CONTACT</span>
</nav>
<div class="join">Join Us</div>
<h1 class="hero-title">INFORM.<br><b>INFLUENCE.</b><br>SELL</h1>
<p class="hero-copy">Lorem ipsum dolor sit amet, consectetur adipisicing elit, sed do eiusmod tempor incididunt ut labore et dolore.</p>
<div class="btn" style="left:168px;top:447px;width:132px;height:42px">Learn More</div>
<div class="btn btn-ghost" style="left:318px;top:447px;width:130px;height:42px">Contact us</div>
<div class="partners" aria-label="Client badges">
  <span></span><span class="round"></span><span class="round"></span><span class="round"></span><span></span><span></span><span></span><span class="round"></span>
</div>

<!-- CHALLENGE -->
<div class="photo" style="left:108px;top:768px;width:231px;height:331px;background:linear-gradient(160deg,#c8cdd3,#8b8f95)" role="img" aria-label="Photo of two smiling businessmen seated with notebooks"></div>
<div class="photo" style="left:348px;top:842px;width:230px;height:330px;background:linear-gradient(160deg,#e8e4df,#a8a29c)" role="img" aria-label="Photo of a businesswoman taking notes at a meeting"></div>
<div class="eyebrow" style="left:615px;top:836px">The big challenge</div>
<h2 class="title" style="left:615px;top:866px;width:480px">Why you need to have a <b>good Communication</b> skills?</h2>
<p class="copy" style="left:615px;top:962px;width:432px">In today's competitive business environment, effective communication is more essential than ever before. It is the foundation upon which companies are built, careers are propelled, and knowledge is imparted. Effective communication is critical - without it, misunderstandings arise, errors occur, and business goals are frustrated. In short, effective communication is the key driver of long-term business and professional success.</p>
<div class="btn" style="left:615px;top:1129px;width:131px;height:40px">Learn More</div>

<!-- HOW WE HELP -->
<div class="eyebrow" style="left:145px;top:1274px">Grow with us</div>
<h2 class="title" style="left:145px;top:1304px">How we <b>help?</b></h2>
<p class="copy" style="left:145px;top:1363px;width:408px">At Lantern &amp; Loomly, we help individuals and organizations “get what they want” through clear and persuasive communication. Our consulting, coaching, and training services help clients achieve targeted business objectives, with an emphasis on informing, influencing, and selling.</p>
<div class="btn" style="left:145px;top:1486px;width:131px;height:41px">Get Started</div>
<div class="photo" style="left:592px;top:1300px;width:233px;height:304px;background:linear-gradient(160deg,#8a7a6d,#3e4550)" role="img" aria-label="Photo of a presenter in a suit pointing at a whiteboard"></div>
<div class="photo" style="left:836px;top:1274px;width:234px;height:305px;background:linear-gradient(160deg,#e9ecef,#b9bec4)" role="img" aria-label="Photo of a woman presenting charts on a whiteboard"></div>

<!-- SERVICES -->
<section class="services" aria-label="Services"></section>
<div class="eyebrow" style="left:0;top:1740px;width:1200px;text-align:center">Services</div>
<h2 class="title" style="left:0;top:1763px;width:1200px;text-align:center">Our <b>Expertise</b></h2>

<div class="card-img" style="left:59px;top:1846px;background:linear-gradient(160deg,#dfe3e7,#9ea4aa)" role="img" aria-label="Photo of a sales training session"></div>
<div class="card-img" style="left:278px;top:1846px;background:linear-gradient(160deg,#dcdfe2,#8c949c)" role="img" aria-label="Photo of a presentation skills workshop"></div>
<div class="card-img" style="left:498px;top:1846px;background:linear-gradient(160deg,#4a4a4e,#1c1c1e)" role="img" aria-label="Photo of a conference talk badge"></div>
<div class="card-img" style="left:717px;top:1846px;background:linear-gradient(160deg,#e4e4e4,#3a3a3c)" role="img" aria-label="Photo of a card reading elevator pitch"></div>
<div class="card-img" style="left:936px;top:1846px;background:linear-gradient(160deg,#5a4a3e,#1f1a17)" role="img" aria-label="Photo of a speaker at a microphone"></div>
<div class="card-label" style="left:59px;top:2020px">Sales Training</div>
<div class="card-label" style="left:278px;top:2020px">Presentation Skills<br>Training</div>
<div class="card-label" style="left:498px;top:2020px">Stage Talks</div>
<div class="card-label" style="left:717px;top:2020px">Elevator Pitches</div>
<div class="card-label" style="left:936px;top:2020px">Keynote Speeches</div>

<div class="card-img" style="left:59px;top:2083px;background:linear-gradient(160deg,#1e5f9a,#0b2746)" role="img" aria-label="Illustration of marketing collateral icons"></div>
<div class="card-img" style="left:278px;top:2083px;background:linear-gradient(160deg,#c6b9a8,#6e6256)" role="img" aria-label="Photo of a business presentation in an office"></div>
<div class="card-img" style="left:498px;top:2083px;background:linear-gradient(160deg,#e6e8ea,#7e7a76)" role="img" aria-label="Photo of a team meeting around a table"></div>
<div class="card-img" style="left:717px;top:2083px;background:linear-gradient(160deg,#b7bcc2,#4c4f54)" role="img" aria-label="Photo of colleagues discussing at a desk"></div>
<div class="card-img" style="left:936px;top:2083px;background:linear-gradient(160deg,#4b5a46,#1d231c)" role="img" aria-label="Photo of a man holding a laptop"></div>
<div class="card-label" style="left:59px;top:2262px">Marketing Collateral</div>
<div class="card-label" style="left:278px;top:2262px">Business Presentations<br>&amp; Decks</div>
<div class="card-label" style="left:498px;top:2262px">Venture Capital<br>Presentations &amp; Decks</div>
<div class="card-label" style="left:717px;top:2262px">Convention &amp; Trade<br>Show Messaging</div>
<div class="card-label" style="left:936px;top:2262px">Corporate &amp; Website<br>Messaging</div>

<!-- RESULTS -->
<div class="eyebrow" style="left:160px;top:2486px">Achieve your goal with us</div>
<h2 class="title" style="left:160px;top:2517px">We are know <b>for our results</b></h2>
<p class="copy" style="left:160px;top:2583px;width:410px">Whatever the message, and whatever the medium, we help clients establish a connection, make an impression, and drive audiences toward a predetermined course of action. This results in clear messaging, captivated audiences, and increased sales.</p>
<div class="btn" style="left:160px;top:2705px;width:131px;height:41px">Learn More</div>
<div class="photo" style="left:606px;top:2432px;width:284px;height:359px;background:linear-gradient(160deg,#b07a5e,#4a4f57)" role="img" aria-label="Photo of a team working in a brick-walled office"></div>
<div class="photo" style="left:786px;top:2552px;width:287px;height:262px;background:linear-gradient(160deg,#cbb9a6,#3e4c63)" role="img" aria-label="Photo of a confident businessman in a blue jacket"></div>

<!-- TESTIMONIALS -->
<div class="eyebrow" style="left:0;top:2907px;width:1200px;text-align:center">Testimonials</div>
<h2 class="title" style="left:0;top:2933px;width:1200px;text-align:center">Our <b>Expertise</b></h2>

<div class="t-card" style="left:74px;top:3025px;width:244px;height:198px">
  <svg class="qmark" width="48" height="42" viewBox="0 0 48 42"><path d="M0 0h20v24l-10 18H2l6-18H0z M27 0h21v24l-10 18h-8l6-18h-9z" fill="#00aeef"/></svg>
  <p class="t-quote">Hi Daniel - I love the direction and the changes you made to our marketing materials!</p>
  <p class="t-name">Morgan T.</p>
  <p class="t-role">CEO Brightline Weekly,<br>President Orbit Media Group</p>
</div>
<div class="t-card" style="left:335px;top:3025px;width:243px;height:287px">
  <svg class="qmark" width="48" height="42" viewBox="0 0 48 42"><path d="M0 0h20v24l-10 18H2l6-18H0z M27 0h21v24l-10 18h-8l6-18h-9z" fill="#00aeef"/></svg>
  <p class="t-quote">Thank you, Daniel! I'll likely make adjustments to ensure the key operational details jump out, but I think you nailed the messaging - much more excitement and energy.</p>
  <p class="t-name">Ellis Navarro</p>
  <p class="t-role">Analyst, NoteHarbor</p>
</div>
<div class="t-card" style="left:594px;top:3025px;width:246px;height:264px">
  <svg class="qmark" width="48" height="42" viewBox="0 0 48 42"><path d="M0 0h20v24l-10 18H2l6-18H0z M27 0h21v24l-10 18h-8l6-18h-9z" fill="#00aeef"/></svg>
  <p class="t-quote">Dear Daniel - Thank you for your input! I truly appreciated your tips - frankly, it blew my mind (in a good way). I'm still thinking about our conversation.</p>
  <p class="t-name">Priya R.</p>
  <p class="t-role">Marketing Director,<br>Cobalt Stage Co.</p>
</div>
<div class="t-card" style="left:854px;top:3025px;width:245px;height:249px">
  <svg class="qmark" width="48" height="42" viewBox="0 0 48 42"><path d="M0 0h20v24l-10 18H2l6-18H0z M27 0h21v24l-10 18h-8l6-18h-9z" fill="#00aeef"/></svg>
  <p class="t-quote">Daniel - Thanks a lot for your input and advice. Your suggestions will make a material difference in how I structure and present my information.</p>
  <p class="t-name">Victor L.</p>
  <p class="t-role">Chief Investment Officer,<br>Kestrel Value Partners</p>
</div>

<!-- FOOTER -->
<footer class="footer" aria-label="Footer"></footer>
<div class="footer-base"></div>

<div class="join-box">
  <div class="abs" style="left:520px;top:0;width:296px;height:239px;background:linear-gradient(100deg,rgba(10,127,199,0),rgba(6,70,140,.55))" role="img" aria-label="Faint image of a hand touching business icons"></div>
  <h2 class="abs" style="left:30px;top:54px;font-size:31px;font-weight:400;color:var(--white)">Join Our <b style="font-weight:800">Community!</b></h2>
  <p class="abs" style="left:30px;top:105px;width:450px;font-size:11.5px;line-height:18px;color:var(--white)">Ut enim ad minim veniam, quis nostrud exercitation ullamco laboris nisi ut aliquip ex ea commodo consequat aute irure.</p>
  <div class="field" style="left:31px;top:155px;width:175px">Name</div>
  <div class="field" style="left:225px;top:155px;width:175px">Email</div>
  <div class="field" style="left:411px;top:155px;width:101px;background:#111;color:var(--white);font-weight:700;padding-left:34px">SUBMIT</div>
</div>

<div class="abs" style="left:177px;top:3680px;font-size:22px;line-height:25px;font-weight:300;color:#d8d8d8">LANTERN &amp;<br>LOOMLY</div>
<p class="abs" style="left:169px;top:3752px;width:250px;font-size:11px;line-height:19px;color:#d0d0d0">Ut enim ad minim veniam, quis nostrud exercitation ullamco laboris nisi ut aliquip ex ea commodo consequat aute irure.</p>
<span class="social" style="left:168px"></span>
<span class="social" style="left:207px"></span>
<span class="social" style="left:246px"></span>
<span class="social" style="left:284px"></span>
<span class="social" style="left:322px"></span>

<div class="f-head" style="left:552px;top:3693px">Quick Links</div>
<span class="f-link" style="left:553px;top:3738px">Home</span>
<span class="f-link" style="left:553px;top:3764px">LoomCamp</span>
<span class="f-link" style="left:553px;top:3790px">Testimonials</span>
<span class="f-link" style="left:553px;top:3817px">Team</span>
<span class="f-link" style="left:553px;top:3843px">Contact</span>

<div class="f-head" style="left:810px;top:3693px">Contact Us</div>
<svg class="abs" style="left:815px;top:3740px" width="12" height="16" viewBox="0 0 12 16"><path d="M6 0a6 6 0 0 0-6 6c0 4.5 6 10 6 10s6-5.5 6-10a6 6 0 0 0-6-6zm0 8.5A2.5 2.5 0 1 1 6 3.5a2.5 2.5 0 0 1 0 5z" fill="#fff"/></svg>
<p class="f-link" style="left:842px;top:3738px;line-height:19px">42 Larkspur Lane,<br>East Harbor,<br>ST 00000</p>
<svg class="abs" style="left:815px;top:3808px" width="13" height="13" viewBox="0 0 24 24"><path d="M6.6 10.8a15.1 15.1 0 0 0 6.6 6.6l2.2-2.2a1 1 0 0 1 1-.25 11.4 11.4 0 0 0 3.6.57 1 1 0 0 1 1 1V20a1 1 0 0 1-1 1A17 17 0 0 1 3 4a1 1 0 0 1 1-1h3.5a1 1 0 0 1 1 1c0 1.25.2 2.45.57 3.6a1 1 0 0 1-.25 1z" fill="#fff"/></svg>
<span class="f-link" style="left:842px;top:3806px">(000)555-0142-000</span>
<svg class="abs" style="left:815px;top:3843px" width="14" height="11" viewBox="0 0 14 11"><rect x=".5" y=".5" width="13" height="10" fill="none" stroke="#fff"/><path d="M.5.5 7 6l6.5-5.5" fill="none" stroke="#fff"/></svg>
<span class="f-link" style="left:842px;top:3840px">hello@lanternandloomly.com</span>

<span class="f-link" style="left:160px;top:3930px;font-size:11px">Copyright ©Lantern&amp;Loomly. All rights reserved.</span>
<span class="f-link" style="left:821px;top:3930px;font-size:11px">Privacy Policy &nbsp;&nbsp; | &nbsp;&nbsp; Terms of conditions</span>

</body>
</html>
```